Bref créative
Business cards, invoice, letterhead
Stationery for baby immunisation service
Professional
Thandeka Zulani
Dr
42 9th Avenue
Brenthill
Johannesburg
drtzulani@kovahealth.co.za
PR 0738261

```html
<!DOCTYPE html>
<html lang="en">
<head>
<meta charset="utf-8">
<title>Tiny Sprouts – Business Card</title>
<link rel="stylesheet" href="https://fonts.googleapis.com/css2?family=Open+Sans:wght@400;600;700&display=swap">
<style>
  :root{
    --bg:#e9ecee;
    --teal:#1aa8a8;
    --teal-dark:#0d8a8c;
    --green:#8dc63f;
    --grey-line:#cfd3d6;
    --ink:#4a4f54;
    --white:#ffffff;
  }
  *{box-sizing:border-box;margin:0;padding:0}
  html,body{width:1200px;height:901px;overflow:hidden}
  body{background:var(--bg);font-family:"Open Sans",Arial,sans-serif;position:relative}
  .card{position:absolute;width:540px;height:308px;border-radius:18px;overflow:hidden;box-shadow:0 10px 30px rgba(0,0,0,.15)}
  .card--back{left:40px;top:296px;background:linear-gradient(135deg,#25b9b7 0%,var(--teal) 50%,var(--teal-dark) 100%)}
  .card--front{left:620px;top:296px;background:var(--white)}

  .brand{position:absolute;display:flex;align-items:center;gap:10px}
  .brand__dot{width:18px;height:18px;border-radius:50%}
  .brand__name{font-weight:700;font-size:38px;letter-spacing:-.5px;line-height:1}
  .tagline{position:absolute;font-size:15px;letter-spacing:.4px}

  .card--back .brand{left:0;right:0;top:118px;justify-content:center}
  .card--back .brand__dot{background:var(--white)}
  .card--back .brand__name{color:var(--white)}
  .card--back .tagline{left:0;right:0;top:168px;text-align:center;color:var(--white)}

  .card--front .brand{left:40px;top:36px}
  .card--front .brand__dot{background:var(--green)}
  .card--front .brand__name{color:var(--teal)}
  .card--front .tagline{left:68px;top:84px;color:var(--green)}

  .band{position:absolute;left:0;top:120px;width:540px;height:22px}

  .address{position:absolute;left:40px;top:166px;font-size:13px;line-height:19px;color:var(--ink)}
  .divider{position:absolute;left:150px;top:166px;width:1px;height:62px;background:var(--grey-line)}
  .contact{position:absolute;left:164px;top:166px;font-size:13px;line-height:19px;color:var(--ink);list-style:none}
  .contact__label{color:var(--green);font-weight:700;margin-right:4px}

  .person{position:absolute;right:40px;top:170px;text-align:right}
  .person__name{font-size:20px;font-weight:700;color:var(--teal-dark)}
  .person__role{font-size:12px;color:var(--ink);margin-top:2px}
</style>
</head>
<body>
  <section class="card card--back" aria-label="Card back">
    <div class="brand"><span class="brand__dot"></span><span class="brand__name">Tiny Sprouts</span></div>
    <p class="tagline">Infancy to early childhood</p>
  </section>

  <section class="card card--front" aria-label="Card front">
    <div class="brand"><span class="brand__dot"></span><span class="brand__name">Tiny Sprouts</span></div>
    <p class="tagline">Infancy to early childhood</p>

    <svg class="band" viewBox="0 0 540 22" aria-hidden="true">
      <polygon points="0,0 150,0 162,14 0,14" fill="var(--green)"/>
      <line x1="162" y1="14" x2="540" y2="14" stroke="var(--grey-line)" stroke-width="1.5"/>
      <polygon points="226,6 540,6 540,22 240,22" fill="var(--teal)"/>
    </svg>

    <address class="address">42 9th Avenue<br>Brenthill<br>Johannesburg</address>
    <span class="divider"></span>
    <ul class="contact">
      <li><span class="contact__label">P :</span>+27 11 555 0142</li>
      <li><span class="contact__label">C :</span>+27 83 555 0176</li>
      <li><span class="contact__label">E :</span>drtzulani@kovahealth.co.za</li>
    </ul>

    <div class="person">
      <p class="person__name">Thandeka Zulani</p>
      <p class="person__role">Doctor</p>
    </div>
  </section>
</body>
</html>
```